Modern business card design for professional copywriter

I'd like a business card design that I can use to have my cards printed out by plink.com as a squared corners business card (see artwork and design guidelines here: https://help.plink.com/hc/en-gb/sections/300481726-PLINK-Product-Templates)

The design should be clean and modern and reflect the colours, tone and branding on my website: https://noravestrel.com.au

Target Market(s)

Professionals, B2B small business owners

Industry/Entity Type

Business

Contact Information for Business Card

Nora Vestrel
m: 0427 593 864
e: nora@noravestrel.com.au
w: noravestrel.com.au

Font styles to use
Sans Serif

Requirements
Must have
• Tagline: "Sharp wordcraft for busy, ambitious business owners"
• Brand colours: fd8000, 009984, 666666 and black
Nice to have

```html
<!DOCTYPE html>
<html lang="en">
<head>
<meta charset="utf-8">
<title>Nora Vestrel – Business Card</title>
<link rel="stylesheet" href="https://fonts.googleapis.com/css2?family=Montserrat:wght@400;600;700&display=swap">
<style>
  :root {
    --page: #ffffff;
    --card: #000000;
    --ink: #ffffff;
    --brand-orange: #fd8000;
    --brand-teal: #009984;
    --brand-grey: #666666;
  }
  * { box-sizing: border-box; margin: 0; padding: 0; }
  html, body {
    width: 1200px;
    height: 802px;
    overflow: hidden;
    background: var(--page);
    font-family: "Montserrat", Arial, sans-serif;
  }
  .canvas { position: relative; width: 1200px; height: 802px; }
  .card {
    position: absolute;
    left: 394px;
    width: 576px;
    height: 329px;
    background: var(--card);
    border-radius: 14px;
    color: var(--ink);
  }
  .card--front { top: 63px; }
  .card--back { top: 420px; }

  .brand {
    position: absolute;
    display: flex;
    align-items: center;
    gap: 8px;
    color: var(--brand-teal);
    font-weight: 600;
    white-space: nowrap;
  }
  .brand__dot {
    width: 14px; height: 14px;
    border-radius: 50%;
    background: var(--brand-orange);
    flex: none;
  }
  .card--front .brand { left: 44px; top: 175px; font-size: 28px; }
  .card--back .brand {
    left: 50%; top: 132px; font-size: 27px;
    transform: translateX(-50%);
  }

  .contact { position: absolute; left: 320px; top: 132px; }
  .contact__name {
    font-size: 24px;
    font-weight: 700;
    letter-spacing: 0.3px;
    margin-bottom: 22px;
  }
  .contact__list { list-style: none; }
  .contact__item {
    display: flex;
    align-items: center;
    gap: 10px;
    font-size: 16px;
    line-height: 20px;
    letter-spacing: 0.2px;
  }
  .contact__icon { width: 15px; height: 15px; flex: none; }

  .tagline {
    position: absolute;
    left: 0; right: 0;
    top: 216px;
    text-align: center;
    font-size: 16px;
    letter-spacing: 0.3px;
  }
</style>
</head>
<body>
<main class="canvas">
  <section class="card card--front">
    <div class="brand"><span class="brand__dot"></span>Nora Vestrel</div>
    <div class="contact">
      <h1 class="contact__name">Nora Vestrel</h1>
      <ul class="contact__list">
        <li class="contact__item">
          <svg class="contact__icon" viewBox="0 0 16 16" aria-hidden="true">
            <circle cx="8" cy="8" r="8" fill="#fff"/>
            <rect x="5.2" y="3" width="5.6" height="10" rx="1" fill="#000"/>
            <rect x="6.2" y="4.3" width="3.6" height="6.2" fill="#fff"/>
          </svg>
          <span>0427 593 864</span>
        </li>
        <li class="contact__item">
          <svg class="contact__icon" viewBox="0 0 16 16" aria-hidden="true">
            <circle cx="8" cy="8" r="8" fill="#fff"/>
            <rect x="3.5" y="5" width="9" height="6.5" rx="0.8" fill="none" stroke="#000" stroke-width="1.3"/>
            <path d="M3.8 5.4 8 8.8l4.2-3.4" fill="none" stroke="#000" stroke-width="1.3"/>
          </svg>
          <span>nora@noravestrel.com.au</span>
        </li>
        <li class="contact__item">
          <svg class="contact__icon" viewBox="0 0 16 16" aria-hidden="true">
            <circle cx="8" cy="8" r="8" fill="#fff"/>
            <g fill="none" stroke="#000" stroke-width="1">
              <circle cx="8" cy="8" r="4.8"/>
              <ellipse cx="8" cy="8" rx="2" ry="4.8"/>
              <path d="M3.2 8h9.6M4 5.5h8M4 10.5h8"/>
            </g>
          </svg>
          <span>noravestrel.com.au</span>
        </li>
      </ul>
    </div>
  </section>

  <section class="card card--back">
    <div class="brand"><span class="brand__dot"></span>Nora Vestrel</div>
    <p class="tagline">"Sharp wordcraft for busy, ambitious business owners"</p>
  </section>
</main>
</body>
</html>
```